Brightpath Dental Studio

Please go to www.brightpathdentalstudio.example and obtain the current company logo.
Doctors name are
Marita Velbonne, DDS
Denis Kalb, DMD
Addresses are
318 Larchmont Ave
Teaneck, NJ 07666
201-555-0147
And
872 14th St.
West New York, NJ 07093
201-555-0182
Theme of the business card should feel modrrn and similar to the website.
Front side should include company logo, doctors name, addresses, phone numbers.
Back of the card should include blank lines for patient's name. Date and time for next scheduled appointment. And notice of 24-hr cancellation courtesy policy.
Dental

```html
<!DOCTYPE html>
<html lang="en">
<head>
<meta charset="utf-8">
<title>Brightpath Dental Studio – Business Card</title>
<link rel="stylesheet" href="https://fonts.googleapis.com/css2?family=Arimo:wght@400;700&display=swap">
<style>
  :root {
    --navy: #101a4d;
    --ink: #111111;
    --band-grey: #dedede;
    --rule-grey: #b9b9b9;
    --paper: #ffffff;
    --backdrop: #2b2b2b;
    --photo-warm: #e9c6b3;
    --photo-light: #f3e6dc;
    --photo-accent: #d9432a;
  }
  * { box-sizing: border-box; margin: 0; padding: 0; }
  html, body {
    width: 1200px; height: 1200px; overflow: hidden;
    background: var(--backdrop);
    font-family: "Arimo", Arial, sans-serif;
  }
  .canvas {
    width: 1200px; height: 1200px;
    display: flex; flex-direction: column; align-items: center;
    justify-content: center; gap: 90px;
  }
  .card {
    position: relative; width: 860px; height: 491px;
    background: var(--paper); overflow: hidden;
    box-shadow: 0 12px 30px rgba(0,0,0,.45);
  }

  /* Front */
  .doctors-band {
    position: absolute; top: 0; left: 0; right: 0; height: 52px;
    background: var(--band-grey);
    border-bottom: 2px solid var(--rule-grey);
    display: flex; align-items: center; gap: 30px;
    padding-left: 36px;
    color: var(--navy); font-size: 21px;
  }
  .portrait {
    position: absolute; width: 360px; height: 360px; border-radius: 50%;
    right: -40px; top: 70px;
    background:
      radial-gradient(circle at 40% 90%, var(--photo-accent) 0 22%, transparent 23%),
      radial-gradient(circle at 62% 45%, var(--photo-warm) 0 40%, var(--photo-light) 75%);
  }
  .front .brand {
    position: absolute; left: 40px; top: 205px;
    display: flex; align-items: center; gap: 14px;
  }
  .brand-dot { width: 26px; height: 26px; border-radius: 50%; background: var(--navy); flex: none; }
  .brand-name { color: var(--ink); font-weight: 700; white-space: nowrap; }
  .front .brand-name { font-size: 38px; }
  .locations {
    position: absolute; left: 0; right: 0; bottom: 0; height: 128px;
    background: var(--navy); display: flex;
  }
  .location {
    flex: 1; color: var(--paper); text-align: center;
    padding-top: 26px;
  }
  .location + .location { border-left: 4px solid var(--paper); }
  .location-address { font-size: 19px; }
  .location-phone { font-size: 44px; margin-top: 4px; letter-spacing: .5px; }

  /* Back */
  .appointment-fields { position: absolute; left: 48px; top: 48px; color: var(--navy); }
  .field-label { font-size: 32px; }
  .field-label + .field-label { margin-top: 26px; }
  .field-note { font-size: 18px; margin-top: 2px; }
  .back .brand {
    position: absolute; left: 0; right: 0; top: 235px;
    display: flex; justify-content: center; align-items: center; gap: 18px;
  }
  .back .brand-dot { width: 34px; height: 34px; }
  .back .brand-name { font-size: 54px; }
  .policy-band {
    position: absolute; left: 0; right: 0; bottom: 0; height: 110px;
    background: var(--navy); color: var(--paper);
    text-align: center; font-size: 22px; padding-top: 30px;
  }
</style>
</head>
<body>
<main class="canvas">
  <section class="card front" aria-label="Card front">
    <header class="doctors-band">
      <span>Dr. Marita Velbonne, DDS</span><span>&amp;</span><span>Dr. Denis Kalb, DMD</span>
    </header>
    <div class="portrait" role="img" aria-label="Photo of a smiling patient"></div>
    <div class="brand">
      <span class="brand-dot"></span>
      <span class="brand-name">Brightpath Dental Studio</span>
    </div>
    <footer class="locations">
      <div class="location">
        <p class="location-address">872 14th St. West New York, NJ 07093</p>
        <p class="location-phone">201-555-0182</p>
      </div>
      <div class="location">
        <p class="location-address">318 Larchmont Ave Teaneck, NJ 07666</p>
        <p class="location-phone">201-555-0147</p>
      </div>
    </footer>
  </section>

  <section class="card back" aria-label="Card back">
    <div class="appointment-fields">
      <p class="field-label">Patient's name</p>
      <p class="field-label">Date and time</p>
      <p class="field-note">(for next scheduled appointment)</p>
    </div>
    <div class="brand">
      <span class="brand-dot"></span>
      <span class="brand-name">Brightpath Dental Studio</span>
    </div>
    <footer class="policy-band">24-hours cancellation courtesy policy</footer>
  </section>
</main>
</body>
</html>
```